Design some Business Cards for Vorlix Training Business

Hello everyone,

I would like a new business card for my Vorlix training business.
You can view my website, (still under construction) at www.tallowmereskills.com.

The card can be printed 2-sided full colour. Other than that, I'm leaving this open for your creative control.

You can just use filler text for name, address, email and the like.

```html
<!DOCTYPE html>
<html lang="en">
<head>
<meta charset="utf-8">
<title>Tallowmere Skills — Business Card</title>
<link rel="stylesheet" href="https://fonts.googleapis.com/css2?family=Open+Sans:wght@400;600;700&display=swap">
<style>
  :root {
    --page-bg: #e9e6e1;
    --card-top: #fbfbfb;
    --card-bottom: #e4e5e7;
    --ink: #3d3f43;
    --ink-soft: #8a8d92;
    --brand-blue: #3a86d4;
    --badge-dark: #2b2c2f;
    --rule: #d5d7da;
  }
  * { margin: 0; padding: 0; box-sizing: border-box; }
  html, body { width: 1200px; height: 1023px; overflow: hidden; }
  body {
    background: var(--page-bg);
    font-family: "Open Sans", Arial, sans-serif;
    color: var(--ink);
    position: relative;
  }
  .card {
    position: absolute;
    width: 630px;
    height: 360px;
    left: 285px;
    background: linear-gradient(160deg, var(--card-top) 0%, var(--card-bottom) 100%);
    box-shadow: 0 10px 28px rgba(0,0,0,0.18), 0 2px 4px rgba(0,0,0,0.12);
    overflow: hidden;
  }
  .card-front { top: 110px; }
  .card-back { top: 553px; }

  .bubble {
    position: absolute;
    border-radius: 50%;
    background: rgba(255,255,255,0.55);
  }

  /* front */
  .front-brand {
    position: absolute;
    left: 0; top: 0;
    width: 300px; height: 360px;
    border-right: 1px solid var(--rule);
  }
  .wordmark {
    position: absolute;
    display: flex;
    align-items: center;
    gap: 12px;
    color: var(--brand-blue);
    font-weight: 700;
  }
  .front-brand .wordmark { left: 38px; top: 140px; font-size: 27px; line-height: 1.05; }
  .wordmark .marker {
    flex: none;
    background: var(--brand-blue);
  }
  .front-brand .marker { width: 14px; height: 14px; }
  .address {
    position: absolute;
    left: 30px; bottom: 26px;
    display: flex; gap: 10px; align-items: flex-start;
    font-size: 12px; color: var(--ink-soft); line-height: 1.5;
  }

  .front-info { position: absolute; left: 330px; top: 34px; right: 26px; }
  .cert { display: flex; align-items: center; gap: 12px; }
  .cert-badge {
    width: 34px; height: 34px; border-radius: 50%;
    background: var(--badge-dark); flex: none;
  }
  .cert-title { font-size: 20px; font-weight: 400; color: var(--ink); line-height: 1.1; }
  .cert-sub { font-size: 12px; color: var(--ink-soft); }
  .person { margin: 20px 0 0 46px; }
  .person-name { font-size: 21px; font-weight: 600; color: var(--brand-blue); line-height: 1.1; }
  .person-role { font-size: 12px; color: var(--ink-soft); text-align: right; padding-right: 36px; }

  .contact-list { list-style: none; margin-top: 56px; }
  .contact-list li {
    display: flex; align-items: center; gap: 12px;
    font-size: 12.5px; color: var(--ink-soft);
    margin-bottom: 9px;
  }
  .contact-list svg { flex: none; }

  /* back */
  .card-back .wordmark {
    left: 50%; top: 50%;
    transform: translate(-50%, -50%);
    font-size: 48px; gap: 18px;
    white-space: nowrap;
  }
  .card-back .marker { width: 22px; height: 22px; }
</style>
</head>
<body>

<section class="card card-front" aria-label="Business card, front">
  <span class="bubble" style="width:260px;height:200px;left:360px;top:-40px"></span>
  <span class="bubble" style="width:180px;height:150px;left:470px;top:60px"></span>

  <div class="front-brand">
    <div class="wordmark">
      <span class="marker" aria-hidden="true"></span>
      <span>Tallowmere<br>Skills</span>
    </div>
    <div class="address">
      <svg width="12" height="16" viewBox="0 0 12 16" aria-hidden="true">
        <path d="M6 0a6 6 0 0 0-6 6c0 4.5 6 10 6 10s6-5.5 6-10a6 6 0 0 0-6-6zm0 8.5A2.5 2.5 0 1 1 6 3.5a2.5 2.5 0 0 1 0 5z" fill="#9ab8d8"/>
      </svg>
      <div>Address line 1<br>Address line 2</div>
    </div>
  </div>

  <div class="front-info">
    <div class="cert">
      <span class="cert-badge" aria-hidden="true"></span>
      <div>
        <div class="cert-title">Certified Associate</div>
        <div class="cert-sub">Vorlix Systems 10.7</div>
      </div>
    </div>
    <div class="person">
      <div class="person-name">Name Placeholder</div>
      <div class="person-role">Manager</div>
    </div>
    <ul class="contact-list">
      <li>
        <svg width="14" height="14" viewBox="0 0 14 14" aria-hidden="true">
          <rect x="3" y="0.5" width="8" height="13" rx="1.5" fill="#3a86d4"/>
          <rect x="4.5" y="2.5" width="5" height="7" fill="#fff"/>
        </svg>
        123.456.7890
      </li>
      <li>
        <svg width="14" height="14" viewBox="0 0 14 14" aria-hidden="true">
          <rect x="0.5" y="2.5" width="13" height="9" rx="1" fill="#3a86d4"/>
          <path d="M1 3l6 5 6-5" stroke="#fff" stroke-width="1.3" fill="none"/>
        </svg>
        info@yourdomain.com
      </li>
      <li>
        <svg width="14" height="14" viewBox="0 0 14 14" aria-hidden="true">
          <circle cx="7" cy="7" r="6.5" fill="#3a86d4"/>
          <path d="M0.5 7h13M7 0.5c-3 3.5-3 9.5 0 13M7 0.5c3 3.5 3 9.5 0 13" stroke="#fff" stroke-width="1" fill="none"/>
        </svg>
        www.tallowmereskills.com
      </li>
    </ul>
  </div>
</section>

<section class="card card-back" aria-label="Business card, back">
  <span class="bubble" style="width:300px;height:240px;left:300px;top:170px"></span>
  <span class="bubble" style="width:200px;height:170px;left:150px;top:220px"></span>
  <div class="wordmark">
    <span class="marker" aria-hidden="true"></span>
    <span>Tallowmere Skills</span>
  </div>
</section>

</body>
</html>
```